Flyer redesign

We need this flier {Seasonal Care back 2018} redesigned for our 2019 season. It is attached below. New design should look different from current design. Be creative yet still professional.

Requirements
Must have
• Designed in photoshop.
• Should have the same text as current design. Only is "2019" instead of 2018. We want a different look with same info to send our customers next year.
• size: standard letter paper 8.5" x 11"
Nice to have
• Can use optional images provided. Not required though. See our website for more photos. thornbrookmemorial.org. send message through briskdrafts if you want a specific photo.
Should not have
• Do not take current design and just change date or image. Make the design look different.

```html
<!DOCTYPE html>
<html lang="en">
<head>
<meta charset="utf-8">
<title>2019 Gravesite Landscaping Packages – Thornbrook Memorial</title>
<link rel="stylesheet" href="https://fonts.googleapis.com/css2?family=Alegreya:wght@400;500&family=Cormorant+Garamond:wght@500&family=Domine:wght@700&family=Open+Sans:wght@400;700&display=swap">
<style>
  :root {
    --backdrop: #3a3a3a;
    --paper: #ffffff;
    --maroon: #7b1a2c;
    --ink: #1f1f1f;
    --body-ink: #333333;
    --green-dark: #248a3c;
    --green-mid: #35a84a;
    --green-light: #6fc25e;
    --green-label: #2e7d32;
  }
  * { margin: 0; padding: 0; box-sizing: border-box; }
  html, body { width: 1200px; height: 1200px; overflow: hidden; background: var(--backdrop); }
  .flyer {
    position: absolute; left: 160px; top: 38px;
    width: 858px; height: 1111px; background: var(--paper); overflow: hidden;
  }
  .flyer-art { position: absolute; inset: 0; width: 858px; height: 1111px; }
  .title-block {
    position: absolute; left: 494px; top: 248px; width: 328px;
    text-align: center; color: var(--maroon);
    font-family: "Alegreya", Georgia, serif;
  }
  .title-year { font-size: 112px; line-height: 1; font-weight: 500; letter-spacing: -2px; transform: scaleX(.85); }
  .title-text { font-size: 44px; line-height: 40px; margin-top: 6px; transform: scaleX(.88); }
  .package-heading {
    position: absolute; text-align: center; color: var(--maroon);
    font-family: "Cormorant Garamond", Georgia, serif; font-weight: 500;
    font-size: 30px; line-height: 36px; text-transform: uppercase;
    transform: scaleX(.86); white-space: nowrap;
  }
  .heading-seasonal { left: 30px; top: 578px; width: 200px; }
  .heading-basic { left: 262px; top: 586px; width: 240px; }
  .heading-perpetual { left: 574px; top: 588px; width: 260px; }
  .package-label {
    position: absolute; left: 33px; top: 657px; width: 200px; text-align: center;
    font-family: "Open Sans", Arial, sans-serif; font-weight: 700;
    font-size: 13px; line-height: 17px; color: var(--green-label);
  }
  .package-desc {
    position: absolute; left: 46px; top: 704px; width: 222px;
    font-family: "Open Sans", Arial, sans-serif; font-size: 11.5px; line-height: 13.5px; color: var(--body-ink);
  }
  .price-list { position: absolute; left: 60px; top: 772px; width: 140px; text-align: center; list-style: none; }
  .price-item { height: 73px; }
  .price-term { font-family: "Alegreya", Georgia, serif; font-size: 20px; line-height: 22px; color: var(--maroon); }
  .price-amount { font-family: "Domine", Georgia, serif; font-weight: 700; font-size: 33px; line-height: 38px; color: var(--ink); letter-spacing: -1px; }
  .brand {
    position: absolute; left: 0; top: 1016px; width: 858px;
    display: flex; justify-content: center; align-items: center; gap: 22px;
    font-family: "Alegreya", Georgia, serif; font-size: 32px; color: var(--maroon);
    font-variant: small-caps; letter-spacing: .5px;
  }
  .brand-mark { width: 44px; height: 44px; border: 2px solid var(--maroon); border-radius: 50%; }
</style>
</head>
<body>
<main class="flyer">
  <svg class="flyer-art" viewBox="0 0 858 1111" aria-hidden="false">
    <defs>
      <linearGradient id="photoTones" x1="0" y1="0" x2="0" y2="1">
        <stop offset="0" stop-color="#4f8a3a"/>
        <stop offset=".45" stop-color="#7fae5a"/>
        <stop offset=".7" stop-color="#c9cfc4"/>
        <stop offset="1" stop-color="#8fb866"/>
      </linearGradient>
      <linearGradient id="fadedTones" x1="0" y1="0" x2="0" y2="1">
        <stop offset="0" stop-color="#f2f3f1"/>
        <stop offset=".5" stop-color="#e7e9e5"/>
        <stop offset="1" stop-color="#dfe2dc"/>
      </linearGradient>
    </defs>
    <rect class="faded-scene" role="img" aria-label="Faded view of cemetery grounds with rows of headstones and trees" x="0" y="330" width="858" height="781" fill="url(#fadedTones)"/>
    <path class="hero-photo" role="img" aria-label="Photo of a tree-lined cemetery road with headstones and trimmed hedges" d="M0 0 H858 V400 Q560 470 264 490 Q80 470 0 352 Z" fill="url(#photoTones)"/>
    <path class="wave-light" d="M0 350 Q80 470 264 486 Q560 470 858 394 V426 Q560 560 264 562 Q90 550 0 474 Z" fill="var(--green-mid)"/>
    <path class="wave-dark" d="M0 400 Q90 520 264 530 Q560 520 858 410 V426 Q560 560 264 562 Q90 550 0 474 Z" fill="var(--green-dark)"/>
    <circle class="title-badge" cx="658" cy="410" r="162" fill="rgba(238,247,233,.88)" stroke="var(--green-light)" stroke-width="8"/>
    <path class="footer-arc" d="M0 1053 Q429 877 858 1058 V1111 H0 Z" fill="var(--paper)"/>
    <path class="footer-line" d="M0 1053 Q429 877 858 1058" fill="none" stroke="var(--green-dark)" stroke-width="7"/>
  </svg>

  <header class="title-block">
    <div class="title-year">2019</div>
    <div class="title-text">Gravesite<br>Landscaping<br>Packages</div>
  </header>

  <h2 class="package-heading heading-seasonal">Seasonal<br>Care</h2>
  <h2 class="package-heading heading-basic">Basic Care<br>Endowment</h2>
  <h2 class="package-heading heading-perpetual">Perpectual Care<br>Endowment</h2>

  <p class="package-label">SEASONAL LANDSCAPING<br>GRAVE CARE</p>
  <p class="package-desc">Weeding and trimming on your gravesite apporximately every 7 weeks during the growing season:&nbsp; mid- April through mid- October</p>

  <ul class="price-list">
    <li class="price-item"><div class="price-term">3 Years</div><div class="price-amount">$327</div></li>
    <li class="price-item"><div class="price-term">3 Years</div><div class="price-amount">$218</div></li>
    <li class="price-item"><div class="price-term">3 Years</div><div class="price-amount">$109</div></li>
  </ul>

  <footer class="brand">
    <span class="brand-word">Thornbrook</span>
    <span class="brand-mark"></span>
    <span class="brand-word">Memorial</span>
  </footer>
</main>
</body>
</html>
```